Restaurant service company needs a website!

I am looking for a skilled web designer/developer to create a professional, responsive, and easy-to-navigate website for my company, which specializes in servicing restaurant cooking equipment. The site should communicate trust, reliability, and technical expertise to our target audience, restaurant owners, managers, and commercial kitchen operators. I have included the company logos, if any other format for them is needed please let me know.

Target Market(s)

restaurant owners, managers, and commercial kitchen operators

Industry/Entity Type

Commercial Kitchen Equipment Service

Coding

Coded - Design and coding required

Number of Pages Required

1 page

Font styles to use
Serif
Sans Serif

Requirements
Must have
• Contact and service request forms, Click-to-call functionality for mobile, Clean, modern layout with strong visuals, Easy navigation, mobile-friendly
Nice to have
• Testimonials or Reviews, If possible a click-to-text functionality for mobile.
Should not have
• Any mention of Refrigeration or HVAC, "Free Quotes"

```html
<!DOCTYPE html>
<html lang="en">
<head>
<meta charset="utf-8">
<title>Hearthline Service Co. — Commercial Kitchen Equipment Service</title>
<link href="https://fonts.googleapis.com/css2?family=Archivo:wght@400;500;700;800&display=swap" rel="stylesheet">
<style>
:root{
  --orange:#d9642a;
  --orange-dark:#b9511f;
  --ink:#22232b;
  --navy:#2b2c37;
  --navy-deep:#1d1e26;
  --paper:#ffffff;
  --muted:#7b7d86;
  --line:#4a4b57;
  --light-text:#c9cad1;
}
*{box-sizing:border-box;margin:0;padding:0}
html,body{width:1200px;height:3600px;overflow:hidden}
body{font-family:"Archivo",Arial,sans-serif;color:var(--ink);background:var(--navy)}
a{color:inherit;text-decoration:none}
.btn{display:inline-flex;align-items:center;justify-content:center;background:var(--orange);color:#fff;font-weight:700;font-size:15px;border-radius:30px;height:54px;padding:0 34px;border:0;font-family:inherit}

/* header */
.site-header{height:211px;background:var(--paper);display:flex;align-items:center;justify-content:space-between;padding:0 84px}
.brand{display:flex;align-items:center;gap:16px}
.brand-mark{width:58px;height:58px;border-radius:50%;background:var(--orange)}
.brand-name{font-weight:800;font-size:30px;line-height:1.05;color:var(--ink);width:230px}
.header-right{display:flex;flex-direction:column;align-items:flex-end;gap:14px}
.header-contact{font-size:14px;color:var(--muted)}
.header-nav{display:flex;align-items:center;gap:40px;font-weight:700;font-size:17px}
.header-nav .btn{height:52px;padding:0 36px}

.sub-nav{height:75px;background:var(--orange);display:flex;align-items:center;padding:0 100px;gap:72px;color:#fff;font-size:14px;font-weight:500}
.sub-nav .search{margin-left:auto}

/* hero */
.hero{height:694px;position:relative;background:linear-gradient(100deg,#1f2a4a 0%,#3c3f4a 30%,#8b8a88 55%,#b5a79a 75%,#6d5544 100%);display:flex;flex-direction:column;align-items:center;padding-top:220px;color:#fff}
.hero h1{font-size:70px;font-weight:700;line-height:1.08;text-align:center;letter-spacing:-1px;text-shadow:0 2px 12px rgba(0,0,0,.35)}
.hero p{margin-top:30px;font-size:15px;color:#eee}

/* features */
.features{height:403px;background:var(--navy);padding:0 84px;position:relative}
.features-grid{display:grid;grid-template-columns:1fr 1fr;padding-top:90px}
.feature{padding-left:8px;padding-right:40px}
.feature + .feature{border-left:1px solid var(--line);padding-left:36px}
.feature-head{display:flex;gap:18px;align-items:flex-start}
.feature-head h3{color:#fff;font-size:18px;font-weight:700;line-height:1.4}
.feature p{color:var(--light-text);font-size:14px;line-height:1.6;margin:30px 0 36px}
.feature .btn{height:52px;font-size:14px}
.features-rule{position:absolute;left:84px;right:84px;bottom:2px;border-top:1px solid var(--line)}

/* services card */
.services{height:1106px;background:var(--navy);position:relative;padding-top:35px}
.services-band{position:absolute;left:0;right:0;top:626px;height:387px;background:var(--orange)}
.services-card{position:relative;margin:0 84px;height:1055px;background:var(--paper);display:grid;grid-template-columns:488px 1fr;gap:34px;padding:0 0 0 34px}
.col-left{padding-top:70px}
.intro-title{display:flex;gap:14px;color:var(--orange);font-size:26px;font-weight:800;line-height:1.15}
.body-text{font-size:14px;line-height:1.75;color:#5c5e66}
.intro .body-text{margin-top:28px}
.photo{position:relative}
.photo-tag{position:absolute;background:var(--orange);color:#fff;font-size:13px;font-weight:700;padding:14px 22px}
.photo-tech{height:297px;margin-top:66px;background:linear-gradient(120deg,#55586a,#2f3550 45%,#8b8e98)}
.photo-team{height:196px;margin-top:78px;background:linear-gradient(120deg,#9b9ea6,#3a3e52 50%,#b9b2a6)}
.caption{font-size:13px;color:var(--muted);margin-top:26px;line-height:1.6}
.photo-grill{height:312px;background:linear-gradient(110deg,#b8b5b0,#3b4466 45%,#7a5d40 80%)}
.col-right h2{font-size:30px;font-weight:800;line-height:1.15;margin:72px 0 34px;width:330px}
.col-right .body-text{width:460px;margin-bottom:26px}
.link-accent{color:var(--orange);font-weight:700;font-size:14px;margin:-6px 0 26px;display:block}
.card-actions{display:flex;justify-content:space-between;width:444px;margin-top:60px}
.card-actions .btn{height:54px;font-size:14px;padding:0 38px}

/* why */
.why{height:798px;background:var(--navy);display:grid;grid-template-columns:472px 506px;gap:48px;padding:0 90px 0 84px}
.why-left{padding-top:110px}
.why-left h2{color:var(--orange);font-size:34px;font-weight:800}
.why-left .body-text{color:var(--light-text);margin-top:22px}
.why-left .link-accent{margin:24px 0 0}
.why-rule{border-top:1px solid var(--line);margin:66px 0 52px}
.why-left h3{color:#fff;font-size:20px;font-weight:700;display:flex;justify-content:space-between}
.market-list{list-style:none;margin-top:34px}
.market-list li{display:flex;align-items:center;gap:20px;color:var(--light-text);font-size:14px;height:46px}
.market-list li span{flex:1}
.why-left .btn{margin-top:22px}

/* service request form */
.request-box{margin-top:44px;background:var(--navy-deep);height:340px}
.request-box h3{color:#fff;font-size:27px;font-weight:700;padding:40px 30px 0}
.request-form{display:grid;grid-template-columns:1fr 1fr;gap:26px;padding:36px 0 0 6px;margin-right:-4px}
.form-card{background:var(--orange);height:225px;padding:20px 24px;color:#fff;display:flex;flex-direction:column;gap:10px}
.form-card h4{font-size:14px;font-weight:700;margin-bottom:2px}
.form-card input{height:32px;border:1px solid rgba(255,255,255,.7);background:rgba(255,255,255,.12);color:#fff;font-family:inherit;font-size:13px;padding:0 10px;width:100%}
.form-card input::placeholder{color:#fff;opacity:.9}
.form-card .submit{height:34px;background:var(--navy-deep);color:#fff;font-weight:700;font-size:13px;border:0;font-family:inherit;border-radius:20px}
.photo-crew{height:242px;margin-top:50px;background:linear-gradient(110deg,#a9a7a3,#3a3e55 40%,#8b7a6a 70%,#3a3e55)}

/* highlights */
.highlights{height:258px;background:var(--paper);display:grid;grid-template-columns:repeat(3,1fr);padding:70px 84px 0}
.highlight{padding:0 30px;border-left:1px solid #ddd}
.highlight:first-child{border-left:0;padding-left:10px}
.highlight h3{display:flex;align-items:center;gap:14px;font-size:18px;font-weight:800}
.highlight p{font-size:13px;color:var(--muted);margin-top:18px;line-height:1.6}

.site-footer{height:72px;background:var(--navy-deep);display:flex;align-items:center;justify-content:space-between;padding:0 84px;color:var(--light-text);font-size:13px}
.footer-actions{display:flex;gap:22px;align-items:center}
</style>
</head>
<body>

<header class="site-header">
  <a class="brand" href="#">
    <span class="brand-mark"></span>
    <span class="brand-name">Hearthline Service Co.</span>
  </a>
  <div class="header-right">
    <div class="header-contact">Call (555) 014-2290 · Text (555) 014-2291</div>
    <nav class="header-nav">
      <a href="#">Home</a><a href="#">Services</a><a href="#">About</a><a href="#">Contact</a>
      <a class="btn" href="#request">Request Service</a>
    </nav>
  </div>
</header>

<nav class="sub-nav">
  <a href="#">Home</a>
  <a href="#">Services ▾</a>
  <a href="#">Repairs &amp; Maintenance</a>
  <a href="#">Parts ▾</a>
  <a href="#">Emergency Calls</a>
  <svg class="search" width="20" height="20" viewBox="0 0 20 20" fill="none" stroke="#fff" stroke-width="2.2"><circle cx="8" cy="8" r="6"/><path d="M13 13l5 5"/></svg>
</nav>

<section class="hero" role="img" aria-label="Technician in a blue cap and uniform grilling food under a steel hood in a commercial kitchen">
  <h1>Kitchen Equipment Service<br>Your Restaurant Can Trust!</h1>
  <p>Repair and upkeep for ranges, fryers, grills and ovens in busy kitchens.</p>
</section>

<section class="features">
  <div class="features-grid">
    <div class="feature">
      <div class="feature-head">
        <svg width="24" height="28" viewBox="0 0 24 28"><path d="M12 2c2 5 8 8 8 15a8 8 0 0 1-16 0c0-4 3-6 3-9 2 2 3 4 3 6 2-3 3-7 2-12z" fill="var(--orange)"/></svg>
        <h3>Restaurant Kitchen Service<br>Equipment Experts</h3>
      </div>
      <p>Fast repair for ranges, grills and fryers so your line stays<br>running through every shift without delay.</p>
      <a class="btn" href="#request">Book a Visit</a>
    </div>
    <div class="feature">
      <div class="feature-head">
        <svg width="26" height="28" viewBox="0 0 26 28" fill="none" stroke="#fff" stroke-width="2"><rect x="3" y="3" width="20" height="22" rx="2"/><path d="M8 10h10M8 15h10M8 20h6"/></svg>
        <h3>Commercial Equipment Service<br>Scheduled Maintenance</h3>
      </div>
      <p>Planned checks for ovens and cooking lines that keep<br>your kitchen safe and up to code.</p>
      <a class="btn" href="#request">Plan a Visit</a>
    </div>
  </div>
  <div class="features-rule"></div>
</section>

<section class="services">
  <div class="services-band"></div>
  <div class="services-card">
    <div class="col-left">
      <div class="intro">
        <div class="intro-title">
          <svg width="30" height="30" viewBox="0 0 30 30"><path d="M4 22l10-16 4 7 4-3 4 12z" fill="var(--orange)"/></svg>
          <span>Restaurant Kitchen<br>Equipment Service</span>
        </div>
        <p class="body-text">Our certified technicians diagnose and repair every major brand of cooking equipment. We arrive with common parts on the truck, explain the fix in plain words and test the unit before we leave, so your team can get back to cooking.</p>
      </div>
      <div class="photo photo-tech" role="img" aria-label="Technician in blue uniform checking food in a commercial oven">
        <span class="photo-tag" style="left:38px;top:108px">Certified Technicians</span>
      </div>
      <div class="photo photo-team" role="img" aria-label="Chef and technician standing together beside kitchen equipment"></div>
      <p class="caption">Our team works with kitchen staff to plan repairs around service hours.</p>
    </div>
    <div class="col-right">
      <div class="photo photo-grill" role="img" aria-label="Technician in a cap cooking vegetables on a commercial grill">
        <span class="photo-tag" style="right:22px;top:198px">On-Site Repairs</span>
      </div>
      <h2>Commercial Kitchen Equipment</h2>
      <p class="body-text">From gas ranges to combi ovens, we service the equipment your menu depends on. Each visit includes a full safety check and a written report.</p>
      <p class="body-text">Preventive plans cut breakdowns, extend equipment life and keep inspections simple. We set a schedule that fits your hours.</p>
      <p class="body-text">Emergency calls are answered day and night, with clear pricing before work begins.</p>
      <a class="link-accent" href="#">View all equipment we service</a>
      <p class="body-text">Tap to call or text our dispatch team and a technician will confirm your arrival window.</p>
      <div class="card-actions">
        <a class="btn" href="tel:+15550142290">Call Now</a>
        <a class="btn" href="sms:+15550142291">Text Us</a>
      </div>
    </div>
  </div>
</section>

<section class="why">
  <div class="why-left">
    <h2>Why Choose Us</h2>
    <p class="body-text">Licensed technicians, stocked service vans and honest pricing. We treat every kitchen like our own and stand behind every repair.</p>
    <a class="link-accent" href="#">Read our customer reviews</a>
    <div class="why-rule"></div>
    <h3>Who We Serve <svg width="18" height="18" viewBox="0 0 18 18" fill="none" stroke="#fff" stroke-width="2"><path d="M4 9h10M10 5l4 4-4 4"/></svg></h3>
    <ul class="market-list">
      <li><svg width="16" height="16" viewBox="0 0 16 16" fill="none" stroke="#fff" stroke-width="2"><circle cx="8" cy="8" r="6"/></svg><span>Restaurant owners and managers</span><svg width="16" height="14" viewBox="0 0 16 14" fill="#fff"><rect x="1" y="1" width="14" height="12" rx="2"/></svg></li>
      <li><svg width="16" height="16" viewBox="0 0 16 16" fill="none" stroke="#fff" stroke-width="2"><path d="M3 8l3 3 7-7"/></svg><span>Commercial kitchen operators</span><svg width="16" height="14" viewBox="0 0 16 14" fill="#fff"><rect x="1" y="1" width="14" height="12" rx="2"/></svg></li>
      <li><svg width="16" height="16" viewBox="0 0 16 16" fill="none" stroke="#fff" stroke-width="2"><path d="M8 1a5 5 0 0 1 5 5c0 4-5 9-5 9S3 10 3 6a5 5 0 0 1 5-5z"/></svg><span>Hotels, cafés and catering kitchens</span><svg width="16" height="14" viewBox="0 0 16 14" fill="#fff"><rect x="1" y="1" width="14" height="12" rx="2"/></svg></li>
    </ul>
    <a class="btn" href="#request">Request Service</a>
  </div>
  <div class="why-right">
    <div class="request-box" id="request">
      <h3>Request a Service Visit</h3>
      <form class="request-form" action="#" method="post">
        <div class="form-card">
          <h4>Your Details</h4>
          <input type="text" name="name" placeholder="Full name" aria-label="Full name">
          <input type="text" name="restaurant" placeholder="Restaurant name" aria-label="Restaurant name">
          <input type="tel" name="phone" placeholder="Phone number" aria-label="Phone number">
          <input type="email" name="email" placeholder="Email address" aria-label="Email address">
        </div>
        <div class="form-card">
          <h4>Service Needed</h4>
          <input type="text" name="equipment" placeholder="Equipment type" aria-label="Equipment type">
          <input type="text" name="issue" placeholder="Describe the issue" aria-label="Describe the issue">
          <input type="text" name="date" placeholder="Preferred date" aria-label="Preferred date">
          <button class="submit" type="submit">Send Request</button>
        </div>
      </form>
    </div>
    <div class="photo photo-crew" role="img" aria-label="Two technicians in aprons talking beside kitchen equipment">
      <span class="photo-tag" style="right:10px;top:150px">Trusted by Local Kitchens</span>
    </div>
  </div>
</section>

<section class="highlights">
  <div class="highlight">
    <h3><svg width="22" height="22" viewBox="0 0 22 22" fill="none" stroke="var(--orange)" stroke-width="2.4"><rect x="3" y="5" width="16" height="13" rx="2"/><path d="M7 5V3h8v2"/></svg>Professional Service</h3>
    <p>Licensed, insured and trained on<br>all major cooking brands.</p>
  </div>
  <div class="highlight">
    <h3><svg width="22" height="22" viewBox="0 0 22 22" fill="none" stroke="var(--orange)" stroke-width="2.4"><circle cx="11" cy="11" r="8"/><path d="M11 6v5l3 2"/></svg>Flexible Options</h3>
    <p>Repairs, upkeep plans and<br>after-hours emergency calls.</p>
  </div>
  <div class="highlight">
    <h3><svg width="22" height="22" viewBox="0 0 22 22" fill="none" stroke="var(--orange)" stroke-width="2.4"><path d="M5 3h4l2 5-3 2a11 11 0 0 0 4 4l2-3 5 2v4a2 2 0 0 1-2 2A16 16 0 0 1 3 5a2 2 0 0 1 2-2z"/></svg>Trusted Company</h3>
    <p>Call or text (555) 014-2290<br>for a same-day appointment.</p>
  </div>
</section>

<footer class="site-footer">
  <span>© 2025 Hearthline Service Co. &nbsp;|&nbsp; Commercial Kitchen Equipment Service</span>
  <div class="footer-actions">
    <span>Call · Text</span>
    <svg width="16" height="16" viewBox="0 0 16 16"><circle cx="8" cy="8" r="7" fill="var(--light-text)"/></svg>
    <svg width="16" height="16" viewBox="0 0 16 16"><circle cx="8" cy="8" r="7" fill="var(--light-text)"/></svg>
  </div>
</footer>

</body>
</html>
```